FREE Network Assessment image for landing page

This graphic will be on a landing page and on the left will be Text and a download button that we change and control. The graphic for this project will be to the right.
I will add an example of the landing page area so that it makes more sense.

Please include the text from the sample - the font needs to be the same style as what we are using on the left side!

The graphic needs to be a .png file, roughly 713 x 527 white background. Use discretion on design layout.

Colors are black, Red = PMS 1795 and Gray = Cool Gray 10

Thanks,
Tom Farrow

Target Market(s)

small businesses

Industry/Entity Type

Information Technology

Font styles to use
Other font styles liked:
• See sample

Requirements
Must have
• see description
Nice to have
• Possibly small technology related image to help enhance the text but I don't want any image to compete with the text. Keep in mind the colors mentioned in the description - this is the web site colors.
Should not have
• Should not be hard to read

```html
<!DOCTYPE html>
<html lang="en">
<head>
<meta charset="utf-8">
<title>Free Network Assessment</title>
<link rel="stylesheet" href="https://fonts.googleapis.com/css2?family=Source+Sans+3:wght@400&display=swap">
<style>
  :root {
    --bubble: #4d4d4d;
    --bubble-text: #ffffff;
    --accent: #e8443a;
    --line: #3a3a3a;
    --device: #4a4a4a;
    --page: #ffffff;
  }
  html, body {
    margin: 0;
    padding: 0;
    overflow: hidden;
    background: var(--page);
  }
  .canvas {
    position: relative;
    width: 1200px;
    height: 1000px;
    overflow: hidden;
    background: var(--page);
    font-family: "Source Sans 3", "Myriad Pro", Arial, sans-serif;
  }
  .connectors {
    position: absolute;
    inset: 0;
  }
  .feature {
    position: absolute;
    width: 206px;
    height: 206px;
    border-radius: 50%;
    background: var(--bubble);
    color: var(--bubble-text);
    display: flex;
    align-items: center;
    justify-content: center;
    text-align: center;
    font-size: 15.5px;
    line-height: 1.33;
    margin: 0;
  }
  .feature--speed   { left: 474px; top: 147px; }
  .feature--access  { left: 172px; top: 280px; }
  .feature--security{ left: 63px;  top: 510px; font-size: 14.5px; }
  .feature--tuning  { left: 790px; top: 262px; }
  .feature--backup  { left: 892px; top: 507px; }
</style>
</head>
<body>
<div class="canvas">
  <svg class="connectors" width="1200" height="1000" viewBox="0 0 1200 1000">
    <!-- workstation area -->
    <rect class="workstation" x="380" y="457" width="398" height="276" rx="8" fill="var(--device)" role="img" aria-label="Desktop monitor showing a website layout"/>

    <g fill="none" stroke="var(--line)" stroke-width="2" stroke-dasharray="2 4">
      <line x1="580" y1="366" x2="580" y2="436"/>
      <polyline points="273,492 273,529 361,529"/>
      <line x1="282" y1="621" x2="361" y2="621"/>
      <polyline points="882,493 882,525 800,525"/>
      <line x1="800" y1="618" x2="880" y2="618"/>
    </g>
    <g fill="var(--page)" stroke="var(--line)" stroke-width="2">
      <circle cx="580" cy="442" r="5.5"/>
      <circle cx="367" cy="530" r="5.5"/>
      <circle cx="367" cy="621" r="5.5"/>
      <circle cx="794" cy="526" r="5.5"/>
      <circle cx="794" cy="618" r="5.5"/>
    </g>

    <!-- speed icon -->
    <g class="icon-speed" fill="var(--accent)">
      <circle cx="551" cy="415" r="18" fill="none" stroke="var(--accent)" stroke-width="4" stroke-dasharray="70 8"/>
      <path d="M544 404 v10 a7 7 0 0 0 14 0 v-10 h-3 v8 h-8 v-8z M548 420 h6 v12 h-6z"/>
    </g>
    <!-- lock icon -->
    <g class="icon-lock" fill="var(--accent)">
      <path d="M326 500 v-5 a7 7 0 0 1 14 0 v5" fill="none" stroke="var(--accent)" stroke-width="3.5"/>
      <rect x="323" y="499" width="20" height="21" rx="4"/>
    </g>
    <!-- shield icon -->
    <path class="icon-shield" fill="var(--accent)" d="M322 580 l11 4 v7 c0 7 -5 12 -11 15 c-6 -3 -11 -8 -11 -15 v-7z"/>
    <!-- gears icon -->
    <g class="icon-gears" fill="var(--accent)">
      <circle cx="825" cy="498" r="11" stroke="var(--accent)" stroke-width="5" stroke-dasharray="3 2.5"/>
      <circle cx="825" cy="498" r="4" fill="var(--page)"/>
      <circle cx="847" cy="486" r="8" stroke="var(--accent)" stroke-width="4" stroke-dasharray="2.5 2"/>
      <circle cx="847" cy="486" r="3" fill="var(--page)"/>
    </g>
    <!-- database icon -->
    <g class="icon-database" fill="var(--accent)">
      <ellipse cx="842" cy="575" rx="13" ry="4"/>
      <rect x="829" y="579" width="26" height="6" rx="3"/>
      <rect x="829" y="587" width="26" height="6" rx="3"/>
      <rect x="829" y="595" width="22" height="6" rx="3"/>
      <circle cx="853" cy="594" r="5" stroke="var(--page)" stroke-width="1.5"/>
    </g>
  </svg>

  <p class="feature feature--speed">Perform network and<br>Internet speed test</p>
  <p class="feature feature--access">See who and<br>what has accessto<br>your network and data</p>
  <p class="feature feature--security">Check your network’s<br>security against<br>hacker attacks,<br>theft,ransomware, viruses,<br>and more</p>
  <p class="feature feature--tuning">Resolve PC slowness<br>issues, security<br>vulnerabilities and<br>improper configurations</p>
  <p class="feature feature--backup">Validate your backups<br>are working and<br>recoverable in a<br>timely fashion</p>
</div>
</body>
</html>
```